'CALVENTO' NEW WINE LABEL DESIGN

I am looking for an exceptional and exciting design for a wine label called 'Calvento' meaning 'Lookout'. The design must feature the name 'Calvento', and the word 'Cabernet Sauvignon' in version 1 and 'Sauvignon Blanc' in version 2. It will also need the words 'Valle Central, Chile' at the bottom of the label as a prominent piece of information as well as the vintage 2017. Please produce the work in size 80mm x 100mm. Feel free to use colour in addition to black/white and ensue that the label is easy to read on a shelf placement.
Target Market(s)
SUPERMARKETS & WINE STORES
Requirements
Must have
- EASY TO READ, USE COLOURS LIKE GREEN FOR SAUVIGNON & RED FOR CABERNET SAUVIGNON
- FULL BOTTLE SHOT MUST BE IN PROVIDED DESIGNS. ALL BOTTLE TOPS SHOULD BE QUORLEX STYLE (SCREW TOP)
- PLEASE NOTE THAT LABEL INFORMATION MUSY BE EASY TO READ I.E. VINTAGE, PLACE OF ORGIN ALTHOUGH NOT THE MAIN CONTENT MUST STILL BE CLEAR.
Nice to have
- ARTISTIC REFERENCE LINK TO NAME & ANDES BUT NOT PICTURES OF MOUNTAINS
Should not have
- PICTURES OF GRAPES
- PICTURES OF VINEYARDS
- PICTURES OF MOUNTAINS

```html
<!DOCTYPE html>
<html lang="en">
<head>
<meta charset="utf-8">
<title>Calvento Wine Labels</title>
<link href="https://fonts.googleapis.com/css2?family=Playfair+Display:wght@400;500&family=Oswald:wght@300&display=swap" rel="stylesheet">
<style>
  :root {
    --backdrop: #dcdcda;
    --paper: #f4f4f2;
    --ink: #1b1a1b;
    --band: #1f1f21;
    --ridge-light: #b9b9bb;
    --ridge-mid: #7d7d80;
    --cabernet: #e0242f;
    --blanc: #9cc53b;
    --band-text: #e9e9e9;
  }
  * { margin: 0; padding: 0; box-sizing: border-box; }
  html, body {
    width: 1200px;
    height: 1057px;
    overflow: hidden;
    background: var(--backdrop);
  }
  .label-set {
    position: relative;
    width: 1200px;
    height: 1057px;
    display: flex;
    justify-content: center;
    align-items: center;
    gap: 80px;
  }
  .label {
    position: relative;
    width: 440px;
    height: 550px;
    background: var(--paper);
    border-radius: 8px;
    overflow: hidden;
    box-shadow: 0 6px 18px rgba(0,0,0,0.12);
  }
  .label__brand {
    position: absolute;
    top: 72px;
    left: 0;
    width: 100%;
    text-align: center;
    font-family: "Playfair Display", serif;
    font-weight: 500;
    font-size: 66px;
    letter-spacing: -1px;
    color: var(--ink);
    line-height: 1;
  }
  .label__variety {
    position: absolute;
    top: 150px;
    left: 0;
    width: 100%;
    text-align: center;
    font-family: "Oswald", sans-serif;
    font-weight: 300;
    font-size: 23px;
    line-height: 1;
  }
  .label--cabernet .label__variety { color: var(--cabernet); }
  .label--blanc .label__variety { color: var(--blanc); }
  .label__ridge {
    position: absolute;
    top: 225px;
    left: 0;
    width: 100%;
    height: 175px;
  }
  .label--cabernet .label__ridge {
    background: linear-gradient(180deg, var(--paper) 0%, var(--ridge-light) 30%, var(--cabernet) 62%, var(--band) 100%);
  }
  .label--blanc .label__ridge {
    background: linear-gradient(180deg, var(--paper) 0%, var(--ridge-light) 30%, var(--blanc) 62%, var(--band) 100%);
  }
  .label__band {
    position: absolute;
    top: 400px;
    left: 0;
    width: 100%;
    height: 150px;
    background: var(--band);
    text-align: center;
    color: var(--band-text);
    font-family: "Playfair Display", serif;
  }
  .label__origin {
    position: absolute;
    top: 18px;
    left: 0;
    width: 100%;
    font-size: 16px;
    line-height: 1;
  }
  .label__vintage {
    position: absolute;
    top: 48px;
    left: 0;
    width: 100%;
    font-size: 38px;
    line-height: 1;
  }
</style>
</head>
<body>
  <main class="label-set">
    <section class="label label--cabernet">
      <h1 class="label__brand">CALVENTO</h1>
      <p class="label__variety">Cabernet Sauvignon</p>
      <div class="label__ridge" role="img" aria-label="Layered grey mountain ridges with a red central peak"></div>
      <div class="label__band">
        <p class="label__origin">Valle Central, Chile</p>
        <p class="label__vintage">2017</p>
      </div>
    </section>
    <section class="label label--blanc">
      <h1 class="label__brand">CALVENTO</h1>
      <p class="label__variety">Sauvignon Blanc</p>
      <div class="label__ridge" role="img" aria-label="Layered grey mountain ridges with a green central peak"></div>
      <div class="label__band">
        <p class="label__origin">Valle Central, Chile</p>
        <p class="label__vintage">2017</p>
      </div>
    </section>
  </main>
</body>
</html>
```